"Client Services Packet" Folder design for Hair Tissue Mineral Analysis Company

We are looking for an updated folder design which we use mail our new clients information and starter kits for our services. We are looking for a clean and simple design to match our new logo. We would like our logo along with "Client Services Packet" on the front cover with our company information located inside the folder.
Logo file and color palette will be uploaded in the brief.
**Folder will not need the business card cutout shown on current folder**
Address:
4718 E. Torvin Street
Calvera, AZ 86914
Phone:
1-602-447-3916
1-800-739-2185
Fax:
1-602-864-5207
Website:
www.quvesko.com
Email:
information@quvesko.com

```html
<!DOCTYPE html>
<html lang="en">
<head>
<meta charset="utf-8">
<title>Client Services Packet – Folder</title>
<link href="https://fonts.googleapis.com/css2?family=Orbitron:wght@500&family=Montserrat:wght@400;600&display=swap" rel="stylesheet">
<style>
  :root{
    --page:#e9ebee;
    --navy-deep:#070b16;
    --navy:#0c1a3a;
    --blue:#1d47a8;
    --blue-bright:#2f63d6;
    --title:#3a63c9;
    --paper:#ffffff;
    --paper-shade:#f1f2f4;
    --ink-light:#e8ecf5;
  }
  *{box-sizing:border-box;margin:0;padding:0}
  html,body{width:1200px;height:3000px;overflow:hidden;background:var(--page)}
  body{font-family:"Montserrat",Arial,sans-serif;position:relative}

  .spread{position:absolute;left:80px;width:1040px;height:693px}
  .spread--outer{top:150px}
  .spread--inner{top:1000px}

  .cover-art{position:absolute;inset:0;
    background:
      radial-gradient(ellipse at 20% 30%, rgba(47,99,214,.55), transparent 55%),
      radial-gradient(ellipse at 35% 85%, rgba(47,99,214,.45), transparent 50%),
      linear-gradient(90deg,var(--blue) 0%,var(--navy) 45%,var(--navy-deep) 75%)}
  .spread--outer .cover-art{clip-path:polygon(0 0,100% 0,100% 100%,50.6% 100%,50% 64%,49.4% 100%,0 100%)}

  .glue-tab{position:absolute;width:60px;height:200px;background:linear-gradient(90deg,var(--navy),var(--blue))}
  .glue-tab--left{left:-60px;top:400px;clip-path:polygon(100% 0,0 12%,0 88%,100% 100%)}
  .glue-tab--right{right:-60px;top:400px;background:var(--navy-deep);clip-path:polygon(0 0,100% 12%,100% 88%,0 100%)}

  .brand{position:absolute;font-family:"Montserrat",Arial,sans-serif;font-weight:600;
    color:var(--blue-bright);letter-spacing:.08em;text-transform:uppercase;display:flex;align-items:center;gap:10px}
  .brand__mark{width:14px;height:14px;border-radius:50%;background:var(--blue-bright)}

  .packet-title{position:absolute;font-family:"Orbitron",Arial,sans-serif;font-weight:500;
    color:var(--title);text-align:center;line-height:1.15;letter-spacing:.04em;text-transform:uppercase}

  .spread--outer .brand{right:48px;top:52px;font-size:17px}
  .spread--outer .packet-title{left:560px;width:440px;top:180px;font-size:26px}

  .flap-contact{position:absolute;right:48px;bottom:80px;transform:rotate(180deg);transform-origin:center;text-align:left}
  .flap-contact .brand{position:static;font-size:11px;margin-bottom:6px}
  .flap-contact .brand__mark{width:9px;height:9px}
  .flap-contact .contact{font-size:8.5px;line-height:1.45}

  .fold{position:absolute;left:50%;top:0;bottom:0;width:1px;background:rgba(255,255,255,.08)}

  /* inner */
  .panel{position:absolute;top:0;width:520px;height:693px;background:var(--paper)}
  .panel--left{left:0;background:linear-gradient(90deg,var(--paper-shade),var(--paper))}
  .panel--right{left:520px;border-left:1px solid #dcdee2}
  .pocket{position:absolute;bottom:0;height:200px;width:500px;
    background:
      radial-gradient(ellipse at 80% 20%, rgba(47,99,214,.45), transparent 55%),
      linear-gradient(90deg,var(--navy) 0%,var(--navy-deep) 60%,var(--navy) 100%)}
  .pocket--left{left:0;border-top-right-radius:24px}
  .pocket--right{right:0;border-top-left-radius:24px;padding:48px 0 0 40px}
  .pocket--right .brand{position:static;font-size:14px;margin-bottom:16px}
  .contact{font-size:11.5px;line-height:1.55;color:var(--ink-light)}

  /* closed front */
  .front-cover{position:absolute;left:270px;top:1850px;width:660px;height:880px;
    box-shadow:0 14px 30px rgba(0,0,0,.18)}
  .front-cover .cover-art{background:
      radial-gradient(ellipse at 0% 40%, rgba(47,99,214,.5), transparent 45%),
      linear-gradient(90deg,var(--navy) 0%,var(--navy-deep) 40%,#000 100%)}
  .front-cover .brand{right:50px;top:70px;font-size:19px}
  .front-cover .packet-title{left:0;width:100%;top:300px;font-size:30px}
</style>
</head>
<body>

<section class="spread spread--outer" aria-label="Folder outside spread">
  <div class="glue-tab glue-tab--left"></div>
  <div class="glue-tab glue-tab--right"></div>
  <div class="cover-art" role="img" aria-label="Blue hexagon network with flowing wave lines and glowing orange dots"></div>
  <div class="fold"></div>
  <div class="brand"><span class="brand__mark"></span>Corvane Mineral Labs, Inc.</div>
  <h1 class="packet-title">Client<br>Services<br>Packet</h1>
  <div class="flap-contact">
    <div class="brand"><span class="brand__mark"></span>Corvane Mineral Labs, Inc.</div>
    <p class="contact">
      4718 E. Torvin Street • Calvera, AZ 86914<br>
      Phone: 1-602-447-3916 • 1-800-739-2185<br>
      Fax: 1-602-864-5207<br>
      Website: www.quvesko.com<br>
      Email: information@quvesko.com
    </p>
  </div>
</section>

<section class="spread spread--inner" aria-label="Folder inside spread">
  <div class="panel panel--left">
    <div class="pocket pocket--left" role="img" aria-label="Pocket with blue hexagon network and glowing dots"></div>
  </div>
  <div class="panel panel--right">
    <div class="pocket pocket--right" aria-label="Pocket with company information">
      <div class="brand"><span class="brand__mark"></span>Corvane Mineral Labs, Inc.</div>
      <p class="contact">
        4718 E. Torvin Street • Calvera, AZ 86914<br>
        Phone: 1-602-447-3916 • 1-800-739-2185<br>
        Fax: 1-602-864-5207<br>
        Website: www.quvesko.com<br>
        Email: information@quvesko.com
      </p>
    </div>
  </div>
</section>

<section class="front-cover" aria-label="Folder front cover">
  <div class="cover-art" role="img" aria-label="Blue hexagon network and wave lines fading into black"></div>
  <div class="brand"><span class="brand__mark"></span>Corvane Mineral Labs, Inc.</div>
  <h2 class="packet-title">Client<br>Services<br>Packet</h2>
</section>

</body>
</html>
```